Business Card Design

Sports massage therapist
Would like to convey a simple message.
graphic of human anatomy/muscular system
colours: orange with white/and or grey
glossey

Industry/Entity Type

Business

Contact Information for Business Card

Rhona Whitlow
Soft Tissue Therapist
Sports and Remedial Massage
07915 468302
whitlow.rhona@mailbrook.co.uk

```html
<!DOCTYPE html>
<html lang="en">
<head>
<meta charset="utf-8">
<title>Rhona Whitlow – Sports and Remedial Massage Business Card</title>
<link rel="stylesheet" href="https://fonts.googleapis.com/css2?family=Open+Sans:wght@400;600&display=swap">
<style>
  :root {
    --backdrop: #e9e6e1;
    --card-white: #ffffff;
    --card-grey: #eeeeee;
    --edge-grey: #9fa4a8;
    --orange-deep: #ec9a24;
    --orange-light: #f7c93f;
    --ink: #111111;
    --muscle-deep: #c4512b;
    --muscle-light: #e98a5c;
  }
  * { margin: 0; padding: 0; box-sizing: border-box; }
  html, body {
    width: 1200px; height: 892px; overflow: hidden;
    background: var(--backdrop);
    font-family: "Open Sans", Arial, sans-serif;
  }
  .canvas { position: relative; width: 1200px; height: 892px; }
  .business-card {
    position: absolute; left: 350px; top: 58px;
    width: 500px; height: 776px;
    background: linear-gradient(180deg, var(--card-white) 0%, var(--card-grey) 60%);
    overflow: hidden;
    box-shadow: 0 10px 30px rgba(0,0,0,0.18);
  }
  .card-wave { position: absolute; inset: 0; width: 100%; height: 100%; }
  .service-title {
    position: absolute; top: 34px; left: 0; right: 0;
    text-align: center; color: var(--ink);
    font-size: 43px; font-weight: 400; line-height: 1.12;
  }
  .anatomy-figure {
    position: absolute; left: 180px; top: 225px;
    width: 290px; height: 245px;
    border-radius: 50%;
    background: radial-gradient(ellipse at 55% 40%, var(--muscle-light) 0%, var(--muscle-deep) 100%);
  }
  .therapist {
    position: absolute; left: 34px; top: 490px; color: var(--ink);
  }
  .therapist-name { font-size: 38px; font-weight: 600; line-height: 1.1; }
  .therapist-role { font-size: 23px; font-weight: 400; margin-top: 2px; }
  .contact-list { list-style: none; margin-top: 26px; }
  .contact-item {
    display: flex; align-items: center; gap: 14px;
    font-size: 20px; line-height: 1.5; margin-bottom: 6px;
  }
  .contact-icon {
    width: 26px; height: 22px; flex: none;
    background: var(--ink); border-radius: 3px;
    display: flex; align-items: center; justify-content: center;
  }
</style>
</head>
<body>
<main class="canvas">
  <article class="business-card">
    <svg class="card-wave" viewBox="0 0 500 776" preserveAspectRatio="none" aria-hidden="true">
      <defs>
        <linearGradient id="orangeFill" x1="0" y1="1" x2="1" y2="0">
          <stop offset="0" stop-color="var(--orange-deep)"/>
          <stop offset="1" stop-color="var(--orange-light)"/>
        </linearGradient>
      </defs>
      <path d="M0 250 C120 250 180 330 270 420 C350 500 420 560 500 575 L500 776 L0 776 Z" fill="var(--edge-grey)"/>
      <path d="M0 258 C120 258 180 338 268 428 C348 508 420 568 500 583 L500 776 L0 776 Z" fill="url(#orangeFill)"/>
    </svg>

    <h1 class="service-title">Sports and Remedial<br>Massage</h1>

    <div class="anatomy-figure" role="img" aria-label="Illustration of a running human figure showing the muscular system"></div>

    <section class="therapist">
      <h2 class="therapist-name">Rhona Whitlow</h2>
      <p class="therapist-role">Soft Tissue Therapist</p>
      <ul class="contact-list">
        <li class="contact-item">
          <span class="contact-icon">
            <svg width="14" height="14" viewBox="0 0 24 24" aria-hidden="true"><path fill="#fff" d="M6.6 10.8a15.1 15.1 0 0 0 6.6 6.6l2.2-2.2a1 1 0 0 1 1-.25 11.4 11.4 0 0 0 3.6.57 1 1 0 0 1 1 1V20a1 1 0 0 1-1 1A17 17 0 0 1 3 4a1 1 0 0 1 1-1h3.5a1 1 0 0 1 1 1c0 1.25.2 2.45.57 3.6a1 1 0 0 1-.25 1z"/></svg>
          </span>
          <span>07915 468302</span>
        </li>
        <li class="contact-item">
          <span class="contact-icon">
            <svg width="16" height="12" viewBox="0 0 16 12" aria-hidden="true"><rect x="0.5" y="0.5" width="15" height="11" fill="none" stroke="#fff"/><path d="M0.5 0.5 L8 7 L15.5 0.5" fill="none" stroke="#fff"/></svg>
          </span>
          <span>whitlow.rhona@mailbrook.co.uk</span>
        </li>
      </ul>
    </section>
  </article>
</main>
</body>
</html>
```